Modernise Business Card

Our company has been operating for 10 years. With the start of the new decade we are looking to refresh our business card design. We manufacture a range of industrial product shipping to customers internationally. A copy of our current card, both sides, is attached. We are looking for a mature professional appearance.

```html
<!DOCTYPE html>
<html lang="en">
<head>
<meta charset="utf-8">
<title>Norvex Business Card</title>
<link href="https://fonts.googleapis.com/css2?family=Roboto:wght@400;500;700&display=swap" rel="stylesheet">
<style>
  :root {
    --brand-blue: #03acd6;
    --ink: #1c1c1c;
    --rule-dark: #2a2a2a;
    --paper: #ffffff;
    --backdrop: #2b2b2b;
  }
  * { margin: 0; padding: 0; box-sizing: border-box; }
  html, body { width: 1200px; height: 900px; overflow: hidden; }
  body {
    background: var(--backdrop);
    font-family: 'Roboto', Arial, sans-serif;
    position: relative;
  }
  .card {
    position: absolute;
    width: 525px;
    height: 300px;
    background: var(--paper);
    overflow: hidden;
    box-shadow: 0 12px 30px rgba(0,0,0,0.55);
  }
  /* Front */
  .card-front { left: 80px; top: 100px; }
  .front-band-top {
    position: absolute; left: 0; top: 0; width: 100%; height: 108px;
    background: var(--brand-blue);
    border-bottom: 4px solid var(--rule-dark);
    display: flex; align-items: center; justify-content: center;
  }
  .wordmark {
    font-weight: 700;
    letter-spacing: 1px;
    line-height: 1;
  }
  .front-band-top .wordmark { color: var(--paper); font-size: 62px; }
  .services {
    position: absolute; left: 0; top: 128px; width: 100%;
    text-align: center; list-style: none;
    color: var(--brand-blue); font-size: 17px; line-height: 25px;
    letter-spacing: 0.5px;
  }
  .front-band-bottom {
    position: absolute; left: 0; bottom: 0; width: 100%; height: 62px;
    background: var(--brand-blue);
    border-top: 4px solid var(--rule-dark);
    display: flex; align-items: center; justify-content: center;
  }
  .front-web { color: var(--paper); font-size: 13px; letter-spacing: 0.3px; }

  /* Back */
  .card-back { left: 595px; top: 490px; }
  .card-back .wordmark {
    position: absolute; left: 30px; top: 40px;
    color: var(--brand-blue); font-size: 54px;
  }
  .accent-rule {
    position: absolute; left: 30px; top: 140px; width: 305px; height: 2px;
    background: var(--brand-blue);
  }
  .holder-name {
    position: absolute; right: 28px; top: 126px;
    color: var(--brand-blue); font-size: 19px; font-weight: 700; line-height: 22px;
  }
  .address {
    position: absolute; right: 28px; top: 160px;
    text-align: right; font-size: 12px; line-height: 16px; color: var(--ink);
    font-style: normal;
  }
  .contacts {
    position: absolute; left: 30px; top: 160px; list-style: none;
    font-size: 13px; color: var(--ink);
  }
  .contacts li { display: flex; align-items: center; height: 24px; white-space: nowrap; }
  .contacts svg { width: 13px; height: 13px; margin-right: 12px; fill: var(--brand-blue); flex: none; }
</style>
</head>
<body>
  <section class="card card-front" aria-label="Card front">
    <div class="front-band-top"><span class="wordmark">Norvex</span></div>
    <ul class="services">
      <li>HYDRAULIC ADAPTERS</li>
      <li>HOSE FITTINGS</li>
      <li>QUICK COUPLINGS</li>
    </ul>
    <div class="front-band-bottom"><span class="front-web">www.norvexfittings.com</span></div>
  </section>

  <section class="card card-back" aria-label="Card back">
    <span class="wordmark">Norvex</span>
    <div class="accent-rule"></div>
    <div class="holder-name">Liam Hartley</div>
    <address class="address">
      1208-3, Lin Feng Building<br>
      412 Harbour Road, Jiangbei District<br>
      Haicheng 300100 China
    </address>
    <ul class="contacts">
      <li><svg viewBox="0 0 24 24" aria-hidden="true"><path d="M6.6 10.8a15 15 0 0 0 6.6 6.6l2.2-2.2a1 1 0 0 1 1-.25 11.4 11.4 0 0 0 3.6.57 1 1 0 0 1 1 1V20a1 1 0 0 1-1 1A17 17 0 0 1 3 4a1 1 0 0 1 1-1h3.5a1 1 0 0 1 1 1c0 1.25.2 2.45.57 3.6a1 1 0 0 1-.25 1z"/></svg>+86 138 5520 0417 (China)</li>
      <li><svg viewBox="0 0 24 24" aria-hidden="true"><path d="M3 8c3-3 15-3 18 0v3h-5V9H8v2H3z"/><rect x="5" y="12" width="14" height="9" rx="1"/></svg>+61 402 555 318 (Australia)</li>
      <li><svg viewBox="0 0 24 24" aria-hidden="true"><path d="M2 5h20v14H2z M3 6l9 7 9-7" stroke="#fff" stroke-width="1.5"/></svg>lhartley@norvexfittings.com</li>
      <li><svg viewBox="0 0 24 24" aria-hidden="true"><circle cx="12" cy="12" r="10"/><path d="M2 12h20M12 2c3 3 3 17 0 20M12 2c-3 3-3 17 0 20" stroke="#fff" stroke-width="1.3" fill="none"/></svg>www.norvexfittings.com</li>
    </ul>
  </section>
</body>
</html>
```